Wanderlark Gin - Bottle Label for a craft Gin about to be launched on the world from New Zealand

We are a start up craft distillery in New Zealand. We have developed a wonderful Gin using our own grain spirit and both traditional and New Zealand native botanicals (Manuka to be specific), chosen our bottle and the name "Wanderlark" and done a bit of amateur label design and now we are looking for someone to make it great.

Feel free to change up our amateur concept but give us something that will pop from the back bar and scream authenticity, craft and individuality.

The attached files give you the specifications of the bottle, our current concept for a Wanderlark label and an earlier concept drawing that gives an idea of where we are thinking the two labels should go on the front of the bottle.

Thanks, we look forward to your ideas!!

Target Market(s)

High end and craft Gin drinkers. Hipsters and cocktail barflys and their bar tenders and bar owners

Requirements
Must have
• Attractive individuality
Nice to have
• Coolness
Should not have
• Uncoolness

```html
<!DOCTYPE html>
<html lang="en">
<head>
<meta charset="utf-8">
<title>Wanderlark Gin – Front Label</title>
<link href="https://fonts.googleapis.com/css2?family=Barlow:wght@400;500;700&family=Barlow+Condensed:wght@400;500;600;700&display=swap" rel="stylesheet">
<style>
  :root {
    --ink: #0d0d0d;
    --paper: #ffffff;
    --red: #ef4238;
    --red-deep: #c9372f;
    --cyan: #1ec3e0;
  }
  html, body {
    margin: 0;
    padding: 0;
    width: 927px;
    height: 1200px;
    overflow: hidden;
    background: var(--paper);
  }
  .label {
    position: absolute;
    left: 253px;
    top: 40px;
    width: 420px;
    height: 1120px;
    display: block;
  }
  .shape-ink { fill: var(--ink); }
  .shape-red { fill: var(--red); }
  .rule { stroke: var(--cyan); stroke-width: 2.5; }
  .origin-line {
    font-family: "Barlow", sans-serif;
    font-weight: 700;
    font-size: 20px;
    letter-spacing: 2px;
    fill: var(--red);
  }
  .brand-name {
    font-family: "Barlow Condensed", sans-serif;
    font-weight: 600;
    font-size: 76px;
    letter-spacing: 1px;
    fill: var(--paper);
  }
  .volume {
    font-family: "Barlow Condensed", sans-serif;
    font-size: 21px;
    fill: var(--paper);
  }
  .volume .unit { font-weight: 700; }
  .recipe-tab-text {
    font-family: "Barlow", sans-serif;
    font-weight: 700;
    font-size: 19px;
    letter-spacing: 1px;
    fill: var(--paper);
  }
  .recipe-number { font-size: 24px; }
  .description {
    font-family: "Barlow", sans-serif;
    font-weight: 400;
    font-size: 19px;
    fill: var(--paper);
  }
  .spec {
    font-family: "Barlow Condensed", sans-serif;
    font-weight: 400;
    font-size: 21px;
    letter-spacing: 0.5px;
    fill: var(--paper);
  }
</style>
</head>
<body>
<svg class="label" viewBox="0 0 390 1040" xmlns="http://www.w3.org/2000/svg" aria-labelledby="label-title">
  <title id="label-title">Wanderlark New Zealand Small Batch Gin label</title>
  <defs>
    <linearGradient id="botanical-fill" x1="0" y1="0" x2="1" y2="1">
      <stop offset="0" stop-color="#ef4238"/>
      <stop offset="1" stop-color="#d63c33"/>
    </linearGradient>
  </defs>

  <!-- upper panel -->
  <polygon class="shape-ink" points="195,3 360,75 360,530 195,600 30,530 30,75"/>

  <!-- name block -->
  <text class="origin-line" x="195" y="150" text-anchor="middle">NEW ZEALAND</text>
  <text class="brand-name" x="195" y="232" text-anchor="middle" textLength="300" lengthAdjust="spacingAndGlyphs">WANDERLARK</text>
  <text class="origin-line" x="195" y="272" text-anchor="middle">SMALL BATCH GIN</text>

  <!-- botanical illustration area -->
  <rect x="40" y="320" width="310" height="195" rx="4" fill="url(#botanical-fill)" role="img" aria-label="Red silhouette illustration of manuka flowers and native leaves"/>

  <text class="volume" x="195" y="556" text-anchor="middle">500<tspan class="unit">ML</tspan></text>

  <!-- lower panel -->
  <polygon class="shape-ink" points="30,580 195,650 360,580 360,1037 30,1037"/>

  <!-- recipe tab -->
  <polygon class="shape-red" points="137,597 195,621 255,597 255,700 137,700"/>
  <text class="recipe-tab-text" x="196" y="652" text-anchor="middle">RECIPE</text>
  <text class="recipe-tab-text recipe-number" x="196" y="685" text-anchor="middle">#4</text>

  <!-- description -->
  <text class="description" text-anchor="middle">
    <tspan x="195" y="734">A classically inspired gin</tspan>
    <tspan x="195" y="762">with a New Zealand twist.</tspan>
    <tspan x="195" y="791">Distilled in-house starting</tspan>
    <tspan x="195" y="820">with local grain and</tspan>
    <tspan x="195" y="848">finished with 11 botanicals</tspan>
    <tspan x="195" y="877">including a generous</tspan>
    <tspan x="195" y="905">helping of east coast manuka</tspan>
    <tspan x="195" y="934">cones, gisborne citrus</tspan>
    <tspan x="195" y="962">and otago lavender.</tspan>
  </text>

  <line class="rule" x1="48" y1="983" x2="344" y2="983"/>
  <text class="spec" x="56" y="1019">84 PROOF</text>
  <text class="spec" x="336" y="1019" text-anchor="end">42% ALC. BY VOL.</text>
</svg>
</body>
</html>
```